One of Australia's fastest growing energy maintenance contractors needs a new website

www.brightpane.com.au
Our business has evolved over the past years and now our website is no longer relevant.
We clean solar panels and we vacuum roof gutters.
We clean solar panels on the roofs of residential houses right up to billion dollar solar farms with in excess of 1 million panels. We offer thermal image testing and bird proofing for our residential and commercial clients and thermal drone imaging services for our solar farm clients.
We vacuum clean roof gutters (using a LoftSuk) on the residential house next door right up to enormous private and public schools, colleges, shopping centres, strat complexes and commercial buildings.
When first built our business had more of a domestic residential skew and the website reflected that. While that is still part of our core business we are now bidding on and have secured large government, commercial and infrastructure contracts and our new website needs to reflect our growth and our new business. We need a new site that it optimised for both desktop ad phone viewing as our latest figures showed that 73% of people visiting our site are on mobile phones. We have an extensive amount of data on Vesti Metrics available as well as Promos. Both that would also need integrating with the site along with a few other plugins such as Qarlo Chat Desk, Pallio etc along with SEO key words etc. We are also the winner and finalists over multiple years of the small business of the year awards and we like to proudly and prominently display those on our site.
We are looking for a new site with a modern professional feel / theme
There is a definitive break in our business between the solar Panel cleaning clients and the gutter cleaning clients so we would like a home page that begins with a simple choice:
Solar Panel Cleaning – Gutter Cleaning
With a professional full screen background image (we have hundreds to choose from) and along the bottom a small area with rights reserved etc, phone number etc (at some point in the future we will split these into two businesses but for now it’s what we have).
After that selection is made we would like a repeat of that same scenario but the selection is:
If it’s Solar Panel Cleaning
(new background image)
Government – Infrastructure – Commercial – Residential
If it’s Gutter Cleaning
(new background image)
Government – Strata – Commercial – Residential
After making those choices then onto the relevant pages with background images relevant to each sector and a them that suits (on the residential we would like to keep the link to our vesti ratings) - We will provide copy / text for each relevant page.
Other than that, a menu inclusive of the above and:
Resellers Portal – we will provide a link to this from Qarlo CRM)
Customer portal (we will supply a link to this from our booking system)
We also need a page for our Solar Resellers / Partners page but we will give them a link to this, it won’t be listed on the site.
Request a quote page (Again we will provide information from Qarlo as this will be linked to the CRM)
Standard contact us page inclusive of phone numbers, address and fields supplied from CRM
Sydney – 02 7391 5083
Southern Highlands – 02 4860 3178
Goulburn – 02 4860 3178
Canberra – 02 6172 8354
Wollongong – 02 4239 6017
sales@brightpane.com.au
Head Office - Ferndale Rise NSW 2590
ABN: 48906237115
Responsive Design: Optimized for desktop and mobile (73% mobile visitors).
Fast Loading Speed: Optimized for performance.
Smooth Transition Animations: For service and category selection.
Sticky Contact Bar: Always accessible at the bottom of mobile screens for quick calls.
SEO Optimization: Focused on government tenders, large-scale commercial contracts, and infrastructure projects.
Integrations
Vesti Metrics & Vesti Promos.
Qarlo Chat Desk.
Pallio Beacon.
SEO tools and keyword optimization.
Many many more images available if needed

```html
<!DOCTYPE html>
<html lang="en">
<head>
<meta charset="utf-8">
<title>BrightPane – Solar Panel &amp; Gutter Cleaning</title>
<link href="https://fonts.googleapis.com/css2?family=Manrope:wght@300;400;500;600&display=swap" rel="stylesheet">
<style>
  :root {
    --white: #ffffff;
    --brand-blue: #1b8fd8;
    --btn-start: #0b74c9;
    --btn-end: #27aee6;
    --glass: rgba(225, 228, 235, 0.38);
    --glass-border: rgba(255, 255, 255, 0.9);
    --star: #f5b400;
    --footer-start: #0f7fc4;
    --footer-mid: #22a9e1;
    --footer-end: #0a64ad;
    --footer-muted: rgba(255, 255, 255, 0.82);
    --divider: rgba(255, 255, 255, 0.3);
  }
  * { margin: 0; padding: 0; box-sizing: border-box; }
  html, body { width: 1200px; height: 1117px; overflow: hidden; }
  body { font-family: "Manrope", sans-serif; color: var(--white); position: relative; }

  .hero {
    position: absolute; left: 0; top: 0; width: 1200px; height: 853px; overflow: hidden;
  }
  .hero-photo {
    position: absolute; inset: 0;
    background:
      radial-gradient(ellipse at 22% 18%, rgba(70, 100, 60, 0.9) 0%, rgba(70, 100, 60, 0) 40%),
      radial-gradient(ellipse at 80% 35%, rgba(150, 140, 110, 0.7) 0%, rgba(150, 140, 110, 0) 40%),
      radial-gradient(ellipse at 88% 75%, rgba(170, 80, 50, 0.75) 0%, rgba(170, 80, 50, 0) 45%),
      radial-gradient(ellipse at 35% 75%, rgba(40, 55, 95, 0.95) 0%, rgba(40, 55, 95, 0) 55%),
      linear-gradient(180deg, #6f7478 0%, #4d5a55 25%, #3d4766 55%, #4b4860 80%, #6a5560 100%);
  }
  .hero-shade { position: absolute; inset: 0; background: rgba(20, 25, 35, 0.28); }

  .site-header { position: absolute; left: 100px; top: 15px; width: 1000px; height: 43px; }
  .brand { position: absolute; left: 0; top: 0; height: 43px; display: flex; align-items: center; gap: 10px; }
  .brand-mark { width: 30px; height: 30px; background: var(--brand-blue); border-radius: 6px; }
  .brand-name { font-size: 24px; font-weight: 600; color: var(--brand-blue); letter-spacing: 0.2px; }
  .main-nav { position: absolute; right: 0; top: 0; display: flex; align-items: center; height: 43px; }
  .main-nav a { color: var(--white); text-decoration: none; font-size: 13.5px; margin-right: 20px; }
  .quote-btn {
    margin-left: 1px; margin-right: 0 !important; width: 158px; height: 43px; border-radius: 4px;
    background: linear-gradient(90deg, var(--btn-start), var(--btn-end));
    display: flex; align-items: center; justify-content: center;
  }

  .hero-title {
    position: absolute; left: 100px; top: 312px; font-size: 55px; font-weight: 400;
    line-height: 64px; letter-spacing: -0.5px;
  }
  .hero-sub { position: absolute; left: 100px; top: 524px; font-size: 13.5px; font-weight: 400; }

  .service-label { position: absolute; left: 786px; top: 293px; font-size: 17px; font-weight: 400; }
  .service-card {
    position: absolute; top: 333px; width: 224px; height: 228px; border-radius: 17px;
    background: var(--glass); backdrop-filter: blur(10px);
  }
  .service-card.is-active { border: 1.5px solid var(--glass-border); }
  .service-card.solar { left: 633px; }
  .service-card.gutter { left: 877px; }
  .service-icon { position: absolute; left: 21px; top: 28px; }
  .service-name { position: absolute; left: 20px; top: 74px; font-size: 20px; font-weight: 400; line-height: 25px; }
  .service-arrow { position: absolute; left: 24px; top: 172px; }

  .rating-card {
    position: absolute; left: 100px; top: 619px; width: 1001px; height: 168px; border-radius: 17px;
    border: 1.5px solid var(--glass-border); background: var(--glass); backdrop-filter: blur(10px);
  }
  .rating-badge { position: absolute; left: 70px; top: 38px; width: 90px; height: 90px; border-radius: 50%; background: var(--white); opacity: 0.9; }
  .rating-source { position: absolute; left: 186px; top: 35px; font-size: 13.5px; }
  .rating-score { position: absolute; left: 186px; top: 62px; display: flex; align-items: center; gap: 12px; }
  .rating-score .value { font-size: 40px; color: var(--star); font-weight: 400; line-height: 1; }
  .rating-label { position: absolute; left: 186px; top: 117px; font-size: 13.5px; font-weight: 500; }
  .review-count { position: absolute; right: 67px; top: 46px; font-size: 42px; font-weight: 500; line-height: 1; }
  .review-label { position: absolute; right: 67px; top: 103px; font-size: 13.5px; }

  .site-footer {
    position: absolute; left: 0; top: 853px; width: 1200px; height: 264px;
    background: linear-gradient(90deg, var(--footer-start) 0%, var(--footer-mid) 50%, var(--footer-end) 100%);
  }
  .footer-brand { position: absolute; left: 100px; top: 37px; display: flex; align-items: center; gap: 10px; }
  .footer-brand .brand-mark { background: var(--white); width: 34px; height: 34px; }
  .footer-brand .brand-name { color: var(--white); font-size: 25px; }
  .abn { position: absolute; left: 100px; top: 88px; font-size: 13px; }
  .contact-block { position: absolute; top: 50px; font-size: 13.5px; }
  .contact-block dt { font-weight: 500; margin-bottom: 6px; }
  .contact-block dd { color: var(--footer-muted); font-weight: 300; }
  .contact-mail { left: 798px; }
  .contact-office { left: 974px; }
  .footer-divider { position: absolute; left: 100px; top: 119px; width: 1000px; height: 1px; background: var(--divider); }
  .branch-list { position: absolute; left: 100px; top: 134px; width: 1000px; }
  .branch { position: absolute; top: 0; font-size: 13.5px; }
  .branch dt { font-weight: 500; margin-bottom: 6px; }
  .branch dd { color: var(--footer-muted); font-weight: 300; }
  .copyright { position: absolute; left: 0; width: 1200px; top: 211px; text-align: center; font-size: 13.5px; font-weight: 300; }
</style>
</head>
<body>
  <section class="hero">
    <div class="hero-photo" role="img" aria-label="Rows of solar panels on a red corrugated roof with trees and a technician in hi-vis cleaning panels"></div>
    <div class="hero-shade"></div>

    <header class="site-header">
      <div class="brand"><span class="brand-mark"></span><span class="brand-name">BrightPane</span></div>
      <nav class="main-nav">
        <a href="#">Resellers</a>
        <a href="#">Customers</a>
        <a href="#" class="quote-btn">Request A Quote</a>
      </nav>
    </header>

    <h1 class="hero-title">Effortless Clean,<br>Maximum<br>Efficiency</h1>
    <p class="hero-sub">Professional Solar Panel &amp; Gutter Cleaning for Peak Performance</p>

    <p class="service-label">Choose the Service</p>
    <a class="service-card solar is-active" href="#">
      <svg class="service-icon" width="30" height="30" viewBox="0 0 30 30" fill="none" stroke="#fff" stroke-width="1.6">
        <rect x="1" y="1" width="11" height="11" rx="2"/><rect x="17" y="1" width="11" height="11" rx="2"/>
        <rect x="1" y="17" width="11" height="11" rx="2"/><rect x="17" y="17" width="11" height="11" rx="2"/>
      </svg>
      <span class="service-name">Solar Panel<br>Cleaning</span>
      <svg class="service-arrow" width="24" height="20" viewBox="0 0 24 20" fill="none" stroke="#fff" stroke-width="1.8"><path d="M1 10h21M13 1l9 9-9 9"/></svg>
    </a>
    <a class="service-card gutter" href="#">
      <svg class="service-icon" width="24" height="30" viewBox="0 0 24 30" fill="none" stroke="#fff" stroke-width="1.6">
        <path d="M12 2C8 8 3 13 3 19a9 9 0 0 0 18 0c0-6-5-11-9-17z"/><path d="M8 20a4 4 0 0 0 4 4"/>
      </svg>
      <span class="service-name">Gutter Cleaning</span>
      <svg class="service-arrow" width="24" height="20" viewBox="0 0 24 20" fill="none" stroke="#fff" stroke-width="1.8"><path d="M1 10h21M13 1l9 9-9 9"/></svg>
    </a>

    <div class="rating-card">
      <span class="rating-badge"></span>
      <p class="rating-source">Vesti Rating</p>
      <div class="rating-score">
        <span class="value">4.9</span>
        <svg width="128" height="22" viewBox="0 0 128 22" fill="#f5b400">
          <polygon points="11,1 13.6,8 21,8 15,12.5 17.3,20 11,15.5 4.7,20 7,12.5 1,8 8.4,8"/>
          <polygon transform="translate(26.5 0)" points="11,1 13.6,8 21,8 15,12.5 17.3,20 11,15.5 4.7,20 7,12.5 1,8 8.4,8"/>
          <polygon transform="translate(53 0)" points="11,1 13.6,8 21,8 15,12.5 17.3,20 11,15.5 4.7,20 7,12.5 1,8 8.4,8"/>
          <polygon transform="translate(79.5 0)" points="11,1 13.6,8 21,8 15,12.5 17.3,20 11,15.5 4.7,20 7,12.5 1,8 8.4,8"/>
          <polygon transform="translate(106 0)" points="11,1 13.6,8 21,8 15,12.5 17.3,20 11,15.5 4.7,20 7,12.5 1,8 8.4,8"/>
        </svg>
      </div>
      <p class="rating-label">Excellent</p>
      <p class="review-count">392</p>
      <p class="review-label">Reviews</p>
    </div>
  </section>

  <footer class="site-footer">
    <div class="footer-brand"><span class="brand-mark"></span><span class="brand-name">BrightPane</span></div>
    <p class="abn">ABN: 48906237115</p>
    <dl class="contact-block contact-mail"><dt>Mail</dt><dd>sales@brightpane.com.au</dd></dl>
    <dl class="contact-block contact-office"><dt>Head Office</dt><dd>Ferndale Rise NSW 2590</dd></dl>
    <div class="footer-divider"></div>
    <div class="branch-list">
      <dl class="branch" style="left:0"><dt>Sydney</dt><dd>02 7391 5083</dd></dl>
      <dl class="branch" style="left:204px"><dt>Southern Highlands</dt><dd>02 4860 3178</dd></dl>
      <dl class="branch" style="left:408px"><dt>Goulburn</dt><dd>02 4860 3178</dd></dl>
      <dl class="branch" style="left:612px"><dt>Canberra</dt><dd>02 6172 8354</dd></dl>
      <dl class="branch" style="left:816px"><dt>Wollongong</dt><dd>02 4239 6017</dd></dl>
    </div>
    <p class="copyright">© BrightPane 2025, All Rights Reserved.</p>
  </footer>
</body>
</html>
```